Need Polish Flyer

This is a single page advertisement/flyer. The content is attached. This needs to be designed better so that it looks more professional. I have included a trial photo. Because we are using the "Need Cocoa" theme (Google this if you are not familiar) but replacing it with "Need Polish", it is humorous to include the individual looking at a glass of milk. If this works, we will purchase the photo for the final version. You may need to recreate the Brightmoor Dental logo. This is a new company and this was created using Word, so we don't have a high quality version.

```html
<!DOCTYPE html>
<html lang="en">
<head>
<meta charset="utf-8">
<title>Need Polish Flyer</title>
<link rel="stylesheet" href="https://fonts.googleapis.com/css2?family=Roboto+Slab:wght@300;400;600;700;800&display=swap">
<style>
  :root {
    --orange: #d96a2b;
    --ink: #111111;
    --grey-text: #8a8a8a;
    --paper: #ffffff;
    --stage: #e9e8e6;
    --wash-top: #f4f4f5;
    --wash-bottom: #fbfbfb;
    --rule: #333333;
  }
  * { box-sizing: border-box; margin: 0; padding: 0; }
  html, body {
    width: 1200px; height: 2895px; overflow: hidden;
    background: var(--stage);
    font-family: "Roboto Slab", Georgia, serif;
  }
  .flyer {
    position: absolute; left: 82px; top: 722px;
    width: 1035px; height: 1450px;
    background: var(--paper);
    box-shadow: 0 6px 24px rgba(0,0,0,0.12);
    overflow: hidden;
  }
  .flyer > * { position: absolute; }
  .hero-wash {
    left: 0; top: 167px; width: 1035px; height: 630px;
    background: linear-gradient(180deg, var(--wash-top), var(--wash-bottom));
  }
  .brand {
    left: 73px; top: 74px; display: flex; align-items: center; gap: 16px;
    color: var(--orange); font-weight: 700; font-size: 42px; line-height: 1;
  }
  .brand-dot { width: 22px; height: 22px; border-radius: 50%; background: var(--orange); }
  .hero-photo {
    left: 533px; top: 60px; width: 502px; height: 737px;
    background: linear-gradient(180deg, #e6e6e8 0%, #f1f1f1 45%, #dcdcdc 100%);
  }
  .headline { left: 60px; top: 190px; font-weight: 800; line-height: 1.05; }
  .headline .lead { display: block; color: var(--orange); font-size: 100px; }
  .headline .main { display: block; color: var(--ink); font-size: 110px; letter-spacing: -1px; }
  .points { left: 128px; top: 444px; list-style: none; width: 420px; }
  .points li {
    position: relative; font-weight: 700; font-size: 29px; line-height: 41px;
    color: var(--ink); margin-bottom: 24px;
  }
  .points li::before {
    content: ""; position: absolute; left: -33px; top: 20px;
    width: 12px; height: 12px; border-radius: 50%; background: var(--orange);
  }
  .offer-band {
    left: 0; top: 797px; width: 1035px; height: 196px;
    background: var(--orange); text-align: center; color: var(--paper);
  }
  .offer-title { margin-top: 18px; font-weight: 700; font-size: 66px; line-height: 1.1; }
  .offer-title .accent { color: var(--ink); }
  .offer-text { margin-top: 8px; font-weight: 700; font-size: 29px; line-height: 42px; }
  .learn { left: 0; top: 1057px; width: 1035px; text-align: center; }
  .learn-title { color: var(--orange); font-weight: 700; font-size: 29px; line-height: 42px; }
  .learn-body { color: var(--grey-text); font-weight: 300; font-size: 28px; line-height: 42px; }
  .divider { left: 304px; top: 1283px; width: 426px; height: 2px; background: var(--rule); }
  .tagline {
    left: 0; top: 1327px; width: 1035px; text-align: center;
    font-weight: 700; font-size: 46px; color: var(--ink);
  }
  .tagline .accent { color: var(--orange); }
</style>
</head>
<body>
  <main class="flyer">
    <div class="hero-wash"></div>
    <div class="hero-photo" role="img" aria-label="Photo of a man in a grey beanie and glasses holding up a glass of milk"></div>
    <div class="brand"><span class="brand-dot"></span>Brightmoor Dental</div>
    <h1 class="headline"><span class="lead">Need</span><span class="main">Polish?</span></h1>
    <ul class="points">
      <li>Dental plans don’t pay for adult fluoride treatments.</li>
      <li>At $45 a pop, it saves the insurance company a boatload to just say no.</li>
    </ul>
    <section class="offer-band">
      <h2 class="offer-title">We beg to <span class="accent">differ.</span></h2>
      <p class="offer-text">Brightmoor Dental includes fluoride treatments<br>for free for children and adults.</p>
    </section>
    <section class="learn">
      <h3 class="learn-title">Learn something new:</h3>
      <p class="learn-body">When a dentist polishes your teeth, a fluoride treatment<br>provided immediately is scientifically proven to make<br>teeth stronger. Fluoride bonds with the tooth surface to<br>make the most powerful decay prevention known.</p>
    </section>
    <div class="divider"></div>
    <p class="tagline"><span class="accent">Fluoride.</span> It’s not just for kids.</p>
  </main>
</body>
</html>
```